DeskHarbor | A Brightday Company

We need to Develop a Sales Brochure for a coworking space:
1. About DeskHarbor
2. Location
3. Cards to Show Benefits
4. Floor Plan and Pictures
5. Pricing Card

Jersey City Coworking/Shared Office Space, Steps from Linden LINK
Impress your clients. Stimulate your creativity. Unleash your inner genius.
DeskHarbor is Jersey City’s newest premier coworking and shared office space,

home to:

 Entrepreneurs
 Visionaries
 Freelancers
 Consultants
 Telecommuters
 Startups
 + More

Here you’ll have access to everything you need in order to work efficiently, productively, happily and healthily. Essentials, Amenities and Resources
 Furnished office space with 24/7 access
 Conference rooms and meeting spaces
 Networking events and educational workshops
 Business support
 Ultra-High Speed Internet
 Secure WiFi
 Print + Copy + Scan
 Mail service and business address
 White boards and office supplies
 Gourmet teas and coffees
 Kitchen stocked with healthy snacks
 + More

Member Discounts
 Hotel
 Travel
 Car Rental
 Cloud and server
 + More

Our Values

Collaboration, Community, Happiness, Wellness, Growth
Bonus: Our short-term funding program offers financial support to help your business reach its next milestone.
Location and Pricing
DeskHarbor is located at 482 Marlow Court Lane in Jersey City, a prestigious
address on the banks of the Hudson River, just minutes from the Brevard Tunnel and steps from the Linden LINK station.
1. The cover of the brochure should create excitement to open the folder. Do not create a trifold. We are a very high end office space not a medical office. The size of the paper, does not have to be standard. Think card stock, matt or Glossy or Both

2. On Opening the Brochure - The First Page is to educate my client with a art, color and words
3. Page 2,3,4 and 5Is about Inspiration and explanation: I am thinking that they should be cards of detail:
1. Orange: Vision - Consider a theme of Innovation, High Performance, Fun, Value from action, resources, impulse
2. Gold: Details: Orange: Vision - Consider a theme of Authority and Leadership. The duty to Shine, the leader being the backbone of the group. Practial, values of home, status, security, and traditions
3. Blue: Encourage and support, A peacemaker, Think about themes of caring, counseling, nurturing, Idealistic and sympathetic. This is about contribution
4. Green: The Independent thinker, seeking knowledge, intelligence, justice and insight. About the details

The message on these cards should be similar but at various levels of detail

The 5th Card is about Floor Plans - You are not responsible for it this card. Just the Look of how the card should look like

The 6th Card is about pricing
Updates

Project Deadline Extended
Reason: Only 1 designer has provided a decent design. Most of the submissions were recycled and not in line. Please extend by 4 weeks.

Target Market(s)

- Technology Companies (10 people or less)
- Entrepreneurs (2 People)
- Freelancers (1 People)
- small size Technology Company (5 people or less)

Industry/Entity Type

It Company

Font styles to use
Other font styles liked:
• Caviar Dreams and Sans Serif

Requirements
Must have
• - Pictures
• - Details
• - Inspiration
• - FLoor plans
• - Questions and Value
• - Minimal
• Why would they want to buy your product? 
• What's the most important thing it can do for them?
• What is the most important problem your product or service can solve for them?
• To be effective, your brochure needs to get attention, get the prospect interested enough to read further, raise their desire for the product or service, and get them to take a specific action such as buy now, call and make an appointment, return a post card.
Nice to have
• I am open to design - be inspirational
• Should be clear
• They are interested in themselves and/or their own businesses. To get their attention, your brochure needs to focus on the benefits they will enjoy by making a purchase from you.
Should not have
• Cannot be too Salesy
• No Stock pictures
• Don't put a picture of your building on the cover of the brochure
• The only thing they care about is whether or not your products meet their needs.

```html
<!DOCTYPE html>
<html lang="en">
<head>
<meta charset="utf-8">
<title>DeskHarbor Brochure Covers</title>
<link href="https://fonts.googleapis.com/css2?family=Questrial&display=swap" rel="stylesheet">
<style>
  :root {
    --bg: #e9e6e2;
    --paper: #ffffff;
    --paper-shade: #f1f1f1;
    --ink: #8a8a8a;
    --ink-soft: #a9a9a9;
    --orange: #f07b1e;
    --icon: #9a9a9a;
  }
  * { margin: 0; padding: 0; box-sizing: border-box; }
  html, body { width: 1200px; height: 750px; overflow: hidden; }
  body {
    background: var(--bg);
    font-family: "Questrial", sans-serif;
    color: var(--ink);
    position: relative;
  }
  .cover {
    position: absolute;
    width: 540px;
    height: 380px;
    background: linear-gradient(135deg, var(--paper) 60%, var(--paper-shade));
    box-shadow: 0 10px 28px rgba(0,0,0,0.18);
    overflow: hidden;
  }
  .cover--front { left: 40px; top: 185px; }
  .cover--back { left: 620px; top: 185px; }
  .spine {
    position: absolute; left: 0; top: 0; bottom: 0; width: 14px;
    background: linear-gradient(90deg, #e2e2e2, #ffffff);
  }
  .offerings {
    position: absolute; left: 34px; top: 96px;
    font-size: 11px; letter-spacing: 0.3px; color: var(--ink-soft);
  }
  .wave { position: absolute; left: 0; top: 80px; width: 540px; height: 220px; }
  .brand { position: absolute; display: flex; align-items: center; gap: 8px; }
  .brand__dot {
    width: 16px; height: 16px; border-radius: 50%;
    border: 2px solid var(--orange);
  }
  .brand__name { font-size: 24px; color: var(--orange); line-height: 1; }
  .cover--front .brand { right: 40px; top: 40px; }
  .benefits {
    position: absolute; left: 0; right: 0; bottom: 36px;
    text-align: center; font-size: 11px; color: var(--ink);
  }
  .benefits .sep { color: var(--orange); margin: 0 7px; }
  .back-content {
    position: absolute; inset: 0;
    display: flex; flex-direction: column; align-items: center;
    padding-top: 48px;
  }
  .headline {
    color: var(--orange); font-size: 13px; font-weight: 400; letter-spacing: 1px;
    text-transform: uppercase; margin-bottom: 28px;
  }
  .cover--back .brand { position: static; }
  .address {
    margin-top: 30px; text-align: center;
    font-size: 8px; line-height: 1.5; color: var(--ink);
  }
  .phone, .web { font-size: 8px; margin-top: 12px; color: var(--ink); }
  .social { display: flex; gap: 8px; margin-top: 56px; }
  .social span {
    width: 14px; height: 14px; border-radius: 50%; background: var(--icon);
  }
</style>
</head>
<body>
  <section class="cover cover--front">
    <div class="spine"></div>
    <svg class="wave" viewBox="0 0 540 220" role="img" aria-label="Flowing orange and gold smoke artwork across the cover">
      <defs>
        <linearGradient id="waveFill" x1="0" y1="0" x2="1" y2="0">
          <stop offset="0" stop-color="#e8541d" stop-opacity="0.55"/>
          <stop offset="0.35" stop-color="#f7b52a" stop-opacity="0.85"/>
          <stop offset="0.7" stop-color="#f07b1e" stop-opacity="0.75"/>
          <stop offset="1" stop-color="#d9531a" stop-opacity="0.35"/>
        </linearGradient>
      </defs>
      <path d="M0 120 C90 60 170 40 260 70 C350 100 430 40 540 10 L540 90 C450 110 380 170 290 150 C190 130 110 200 0 210 Z" fill="url(#waveFill)"/>
    </svg>
    <p class="offerings">Executive Suites &bull; Office Spaces &bull; CoWorking Space for Startups</p>
    <div class="brand">
      <span class="brand__dot"></span>
      <span class="brand__name">DeskHarbor</span>
    </div>
    <p class="benefits">Impress Your Clients<span class="sep">|</span>Live Inspired<span class="sep">|</span>Stimulate Your Creativity<span class="sep">|</span>Unleash Your Inner Genius</p>
  </section>

  <section class="cover cover--back">
    <div class="back-content">
      <h2 class="headline">Join the Movement</h2>
      <div class="brand">
        <span class="brand__dot"></span>
        <span class="brand__name">DeskHarbor</span>
      </div>
      <p class="address">A Brightday Company<br>482 Marlow Court Lane<br>Marlow Bay, NJ 07999</p>
      <p class="phone">(555) 555-0148</p>
      <p class="web">www.deskharbor.works</p>
      <div class="social" aria-hidden="true">
        <span></span><span></span><span></span><span></span><span></span>
      </div>
    </div>
  </section>
</body>
</html>
```